Visitenkarten-Design für  Softwareunternehmen
Visitenkarten-Design für Softwareunternehmen
Toller Designer! Ist immer auf Vorschläge eingegangen und hat diese umgesetzt. Bin sehr zufrieden mit dem Ergebnis.
Zielgruppe
Wir sind ein B2B Softwareunternehmen, das eine Energiemonitoringsoftware für die mittelständische Industrie entwickelt hat. Das heißt unsere Visitenkarten werden überwiegend an unsere Zielgruppe, d.h. Geschäftsführer produzierender mittelständischer Industrie ausgehändigt.
Aufgabenstellung
Gleichzeitig treten wir nach außen jung, innovativ und voller Tatendrang auf. Ganz nach unserer Vision: Voll Energie. Null Emission. (Auch gerne auf der Visitenkarte mit aufnehmen). Uns ist es wichtig, unser CI nach außen zu kommunizieren und unsere Webseite auf der Visitenkarte zu platzieren.
Die Visitenkarte soll einzeln für jeden MitarbeiterIn personalisiert werden können.

```html
<!DOCTYPE html>
<html lang="de">
<head>
<meta charset="utf-8">
<title>Visitenkarte VOLTARA</title>
<link href="https://fonts.googleapis.com/css2?family=Roboto:wght@400;700&display=swap" rel="stylesheet">
<style>
  :root {
    --page: #e6e7e8;
    --card-white: #ffffff;
    --ink: #34434a;
    --ink-soft: #4a585e;
    --back-light: #5b6b70;
    --back-dark: #1f2a2e;
    --on-dark: #ffffff;
  }
  html, body {
    margin: 0;
    width: 1200px;
    height: 900px;
    overflow: hidden;
    background: var(--page);
    font-family: "Roboto", sans-serif;
  }
  .canvas {
    position: relative;
    width: 1200px;
    height: 900px;
  }
  .card {
    position: absolute;
    left: 277px;
    width: 646px;
    height: 380px;
    box-sizing: border-box;
    box-shadow: 0 10px 28px rgba(0,0,0,0.18);
  }
  .card-front {
    top: 50px;
    background: var(--card-white);
    color: var(--ink);
  }
  .card-back {
    top: 470px;
    background: radial-gradient(ellipse at 25% 20%, var(--back-light) 0%, var(--back-dark) 80%);
    display: flex;
    align-items: center;
    justify-content: center;
  }
  .brand {
    display: flex;
    align-items: center;
    gap: 14px;
    font-weight: 700;
    letter-spacing: 0.12em;
  }
  .brand-square {
    display: block;
    background: currentColor;
  }
  .card-front .brand {
    position: absolute;
    top: 58px;
    left: 0;
    right: 0;
    justify-content: center;
    font-size: 54px;
    color: var(--ink);
  }
  .card-front .brand-square { width: 22px; height: 22px; }
  .card-back .brand {
    font-size: 92px;
    color: var(--on-dark);
  }
  .card-back .brand-square { width: 36px; height: 36px; }
  .details {
    position: absolute;
    top: 196px;
    left: 0;
    right: 0;
    display: flex;
    justify-content: center;
    gap: 24px;
  }
  .person {
    text-align: right;
    padding-top: 20px;
    font-size: 19px;
    line-height: 1.3;
  }
  .person-name { font-weight: 700; font-size: 20px; color: var(--ink-soft); }
  .person-role { font-size: 16px; color: var(--ink-soft); margin-bottom: 8px; }
  .divider {
    width: 2px;
    height: 132px;
    background: var(--ink);
  }
  .contacts {
    list-style: none;
    margin: 0;
    padding: 0;
    font-size: 20px;
    letter-spacing: 0.04em;
  }
  .contacts li {
    display: flex;
    align-items: center;
    gap: 12px;
    height: 32px;
  }
  .contacts svg {
    width: 16px;
    height: 16px;
    fill: var(--ink);
    flex: none;
  }
</style>
</head>
<body>
<main class="canvas">
  <section class="card card-front">
    <div class="brand"><span class="brand-square"></span>VOLTARA</div>
    <div class="details">
      <div class="person">
        <div class="person-name">Jonas Beispiel</div>
        <div class="person-role">Leiter Marketing</div>
        <div>Lindenweg 7</div>
        <div>88410 Talheim</div>
      </div>
      <div class="divider"></div>
      <ul class="contacts">
        <li><svg viewBox="0 0 16 16"><path d="M3 1l3 3-1.5 2c1 2 3 4 5 5l2-1.5 3 3-2 2C6 14 2 10 1 3z"/></svg>07361 402 11 30</li>
        <li><svg viewBox="0 0 16 16"><rect x="4" y="1" width="8" height="4"/><rect x="1" y="6" width="14" height="6" rx="1"/><rect x="4" y="10" width="8" height="5"/></svg>07361 402 11 39</li>
        <li><svg viewBox="0 0 16 16"><path d="M1 3h14v10H1z M1 3l7 6 7-6" fill="none" stroke="#34434a" stroke-width="1.6"/></svg>info@voltara.example</li>
        <li><svg viewBox="0 0 16 16"><g fill="none" stroke="#34434a" stroke-width="1.4"><circle cx="8" cy="8" r="6.5"/><ellipse cx="8" cy="8" rx="3" ry="6.5"/><path d="M1.5 8h13"/></g></svg>www.voltara.example</li>
      </ul>
    </div>
  </section>
  <section class="card card-back">
    <div class="brand"><span class="brand-square"></span>VOLTARA</div>
  </section>
</main>
</body>
</html>
```